Business Card Design Project

We are a tiling/bathroom renovation business based in Brisbane Australia and are looking to get a professional looking business card designed to promote ourselves.

We provide quality workmanship to upgrade/enhance peoples' homes.
Updates

Target Market(s)

Homeowners looking to renovate their bathrooms, or get tiling done. Mostly young adults to elderly who can spare several grand to upgrade their home

Industry/Entity Type

Business

Requirements
Must have
• A bold heading is a must: "Tiling Dorsey & Kell"
Must include these details: "ABN: 38 914 027 166", "BSA Licence: 5830172", "Bretta: 0419 238 571", "Lis: 0438 912 306", "Email: tilingdorseyandkell@mailbox-demo.com", "Let Us Set It Straight".

An abstract geometrical logo that's based around squares and straight lines/arrows because we are a tiling business and our slogan is "Let Us Set It Straight"
Nice to have
• I have attached an image of a logo design I got from markvista-demo.com, and the background from Cardloom-demo.com.au templates I really like together I just need the cut and paste look ironed out.

You are free to play around with different looks and feels but around the same theme as my sample. i.e. simple but striking, minimal but eye catching, or not maybe something unexpected could be perfect who knows?
Should not have
• Photorealism on a business card is a pet peeve. Too much detail for a teeny tiny business card. A Business card should stand out at a distance and you shouldn't have to squint to see it's detail.

```html
<!DOCTYPE html>
<html lang="en">
<head>
<meta charset="utf-8">
<title>Tiling Dorsey &amp; Kell — Business Card Options</title>
<link rel="stylesheet" href="https://fonts.googleapis.com/css2?family=Michroma&family=Questrial&family=Kalam:wght@700&family=Orbitron:wght@600&display=swap">
<style>
  :root {
    --canvas-bg: #ffffff;
    --ink: #151515;
    --ink-soft: #3a3a3a;
    --brand-orange: #f08a1c;
    --tile-floor: #ebebeb;
    --tile-floor-deep: #dcdcdc;
    --swoosh-light: #ffffff;
    --swoosh-dark: #bdbdbd;
    --info-panel: #c9c9c9;
  }
  html, body {
    margin: 0;
    padding: 0;
    width: 1200px;
    height: 800px;
    overflow: hidden;
    background: var(--canvas-bg);
  }
  .presentation {
    position: relative;
    width: 1200px;
    height: 800px;
  }
  .card {
    position: absolute;
    width: 488px;
    height: 285px;
  }
  .card--one   { left: 95px;  top: 105px; }
  .card--two   { left: 615px; top: 105px; }
  .card--three { left: 346px; top: 431px; }

  .brand-title  { font-family: "Michroma", sans-serif; fill: var(--ink); font-size: 29px; font-weight: 400; }
  .brand-sub    { font-family: "Michroma", sans-serif; fill: var(--ink); font-size: 15px; font-weight: 400; }
  .brand-square { fill: var(--brand-orange); }
  .slogan       { font-family: "Kalam", cursive; font-weight: 700; fill: var(--ink); }
  .slogan--wide { font-family: "Orbitron", sans-serif; font-weight: 600; fill: var(--ink); letter-spacing: 5px; }
  .contact      { font-family: "Questrial", sans-serif; fill: var(--ink-soft); font-size: 13.5px; }
  .contact--email { font-size: 10.5px; }
  .licence      { font-family: "Questrial", sans-serif; fill: var(--ink-soft); font-size: 8px; }
  .info-panel   { fill: var(--info-panel); }
  .icon         { fill: var(--ink); }
</style>
</head>
<body>
<main class="presentation">

  <!-- Option one -->
  <svg class="card card--one" viewBox="0 0 488 285" xmlns="http://www.w3.org/2000/svg">
    <defs>
      <linearGradient id="swoosh-a" x1="0" y1="0" x2="0" y2="1">
        <stop offset="0" stop-color="var(--swoosh-light)"/>
        <stop offset="0.55" stop-color="#f1f1f1"/>
        <stop offset="1" stop-color="var(--swoosh-dark)"/>
      </linearGradient>
      <linearGradient id="floor-a" x1="0" y1="0" x2="0" y2="1">
        <stop offset="0" stop-color="var(--tile-floor-deep)"/>
        <stop offset="1" stop-color="var(--tile-floor)"/>
      </linearGradient>
    </defs>
    <rect class="tile-floor" width="488" height="285" fill="url(#floor-a)" role="img" aria-label="Light grey tiled floor in perspective"/>
    <path class="swoosh" d="M0 0H488V92C400 110 300 120 220 148C170 166 110 172 60 150C35 140 15 128 0 122Z" fill="url(#swoosh-a)"/>
    <rect class="brand-square" x="74" y="22" width="62" height="62"/>
    <text class="brand-title" x="210" y="52">TILING</text>
    <text class="brand-sub" x="208" y="77">DORSEY &amp; KELL</text>
    <path id="slogan-path-a" d="M58 104Q120 118 196 120" fill="none"/>
    <text class="slogan" font-size="13"><textPath href="#slogan-path-a">“Let us set it straight”</textPath></text>
    <rect class="info-panel" x="0" y="210" width="163" height="42"/>
    <text class="licence" x="35" y="227">BSA Licence 5830172</text>
    <text class="licence" x="35" y="239">ABN 38 914 027 166</text>
    <path class="icon" d="M300 193h12v3h-2v-2h-8v2h-2zM299 197h14v7h-14zM306 198.5a2.3 2.3 0 1 0 .01 0z"/>
    <text class="contact" x="472" y="205" text-anchor="end">Bretta: 0419 238 571 /</text>
    <text class="contact" x="472" y="224" text-anchor="end">Lis: 0438 912 306</text>
    <path class="icon" d="M262 235h14v9h-14zM263 236l6 4.5 6-4.5" fill-rule="evenodd"/>
    <text class="contact contact--email" x="472" y="243" text-anchor="end">tilingdorseyandkell@mailbox-demo.com</text>
  </svg>

  <!-- Option two -->
  <svg class="card card--two" viewBox="0 0 488 285" xmlns="http://www.w3.org/2000/svg">
    <defs>
      <linearGradient id="swoosh-b" x1="0" y1="0" x2="0" y2="1">
        <stop offset="0" stop-color="var(--swoosh-light)"/>
        <stop offset="0.55" stop-color="#f1f1f1"/>
        <stop offset="1" stop-color="var(--swoosh-dark)"/>
      </linearGradient>
      <linearGradient id="floor-b" x1="0" y1="0" x2="0" y2="1">
        <stop offset="0" stop-color="var(--tile-floor-deep)"/>
        <stop offset="1" stop-color="var(--tile-floor)"/>
      </linearGradient>
    </defs>
    <rect class="tile-floor" width="488" height="285" fill="url(#floor-b)" role="img" aria-label="Light grey tiled floor in perspective"/>
    <path class="swoosh" d="M0 0H488V92C400 110 300 120 220 148C170 166 110 172 60 150C35 140 15 128 0 122Z" fill="url(#swoosh-b)"/>
    <rect class="brand-square" x="74" y="22" width="62" height="62"/>
    <text class="brand-title" x="210" y="52">TILING</text>
    <text class="brand-sub" x="208" y="77">DORSEY &amp; KELL</text>
    <path id="slogan-path-b" d="M50 118Q120 150 218 152" fill="none"/>
    <text class="slogan" font-size="15"><textPath href="#slogan-path-b">“Let us set it straight”</textPath></text>
    <rect class="info-panel" x="0" y="210" width="163" height="42"/>
    <text class="licence" x="35" y="227">BSA Licence 5830172</text>
    <text class="licence" x="35" y="239">ABN 38 914 027 166</text>
    <path class="icon" d="M300 193h12v3h-2v-2h-8v2h-2zM299 197h14v7h-14zM306 198.5a2.3 2.3 0 1 0 .01 0z"/>
    <text class="contact" x="472" y="205" text-anchor="end">Bretta: 0419 238 571 /</text>
    <text class="contact" x="472" y="224" text-anchor="end">Lis: 0438 912 306</text>
    <path class="icon" d="M262 235h14v9h-14zM263 236l6 4.5 6-4.5" fill-rule="evenodd"/>
    <text class="contact contact--email" x="472" y="243" text-anchor="end">tilingdorseyandkell@mailbox-demo.com</text>
  </svg>

  <!-- Option three -->
  <svg class="card card--three" viewBox="0 0 488 285" xmlns="http://www.w3.org/2000/svg">
    <defs>
      <linearGradient id="swoosh-c" x1="0" y1="0" x2="0" y2="1">
        <stop offset="0" stop-color="var(--swoosh-light)"/>
        <stop offset="0.55" stop-color="#f1f1f1"/>
        <stop offset="1" stop-color="var(--swoosh-dark)"/>
      </linearGradient>
      <linearGradient id="floor-c" x1="0" y1="0" x2="0" y2="1">
        <stop offset="0" stop-color="var(--tile-floor-deep)"/>
        <stop offset="1" stop-color="var(--tile-floor)"/>
      </linearGradient>
    </defs>
    <rect class="tile-floor" width="488" height="285" fill="url(#floor-c)" role="img" aria-label="Light grey tiled floor in perspective"/>
    <path class="swoosh" d="M0 0H488V92C400 110 300 120 220 148C170 166 110 172 60 150C35 140 15 128 0 122Z" fill="url(#swoosh-c)"/>
    <rect class="brand-square" x="74" y="22" width="62" height="62"/>
    <text class="brand-title" x="210" y="52">TILING</text>
    <text class="brand-sub" x="208" y="77">DORSEY &amp; KELL</text>
    <path id="slogan-path-c" d="M36 110Q160 152 300 128" fill="none"/>
    <text class="slogan--wide" font-size="15"><textPath href="#slogan-path-c">“Letussetitstraight”</textPath></text>
    <rect class="info-panel" x="0" y="210" width="163" height="42"/>
    <text class="licence" x="35" y="227">BSA Licence 5830172</text>
    <text class="licence" x="35" y="239">ABN 38 914 027 166</text>
    <path class="icon" d="M300 193h12v3h-2v-2h-8v2h-2zM299 197h14v7h-14zM306 198.5a2.3 2.3 0 1 0 .01 0z"/>
    <text class="contact" x="472" y="205" text-anchor="end">Bretta: 0419 238 571 /</text>
    <text class="contact" x="472" y="224" text-anchor="end">Lis: 0438 912 306</text>
    <path class="icon" d="M262 235h14v9h-14zM263 236l6 4.5 6-4.5" fill-rule="evenodd"/>
    <text class="contact contact--email" x="472" y="243" text-anchor="end">tilingdorseyandkell@mailbox-demo.com</text>
  </svg>

</main>
</body>
</html>
```